Inspirational Quote Poster for Employees

For this project, we need a simple yet high-impact poster template that will be customized for each of our employees with a personalized inspirational quote and color scheme. This template should allow us to quickly and easily customize the text and colors in the poster without a lot of effort.

The poster design should consist of:
- A stylized text area to contain the main text of the quote
- A separate text area to contain the source of quote
- A background that complements the color and style of the text

Text may use different typographic effects (such as color, stroke weight, italicization, font size changes, drop shadows) to draw attention to words in the quote; the source of the quote may be formatted the same as the main text of the quote, or may be formatted differently to distinguish it from the main quote.

The background may be simply a single color, subtle texture, gradients, halftone effects, or other color/texture effects may be used to complement the text.

Examples of the types of posters envisioned by this project:
- http://www.pinvelora.example/marcusdtelford/quillbase-job-1/

Sample quotes to use to build your poster - choose whichever one you want, but be certain that the poster design will handle both long and short quotes:
- "Happiness in intelligent people is the rarest thing I know" - Walden Prosket
- "Wanting to be someone else is a waste of the person you are." - Rolf Dintey
- "Experience is not what happens to you. It is what you do with what happens to you." - Ferris Mundell
- "Simplicity is the ultimate in sophistication." - Rinaldo de Pavesco
- "You will get all you want in life if you help enough other people get what they want." - Tad Pomfrey
- "Hell, there are no rules here — we're trying to accomplish something." - Gareth Vullane

Industry/Entity Type

Quote

Requirements
Must have
• Final deliverable must be:
• - Formatted for an 18” x 24” poster (in portrait orientation)
• - Delivered in Adobe InDesign, Adobe Illustrator, or Extended PostScript format
• - Use CMYK color mode
• - Be print-ready at 300dpi resolution
• - Include any fonts used in the template

```html
<!DOCTYPE html>
<html lang="en">
<head>
<meta charset="utf-8">
<title>Quote Poster — Ferris Mundell</title>
<link rel="stylesheet" href="https://fonts.googleapis.com/css2?family=Marcellus&family=PT+Sans+Narrow&display=swap">
<style>
  :root {
    --rust: #b8501a;
    --paper: #ffffff;
    --ink-light: #ffffff;
    --portrait-dark: #3a3a3a;
    --portrait-sepia: #b98a6a;
  }
  * { margin: 0; padding: 0; box-sizing: border-box; }
  html, body { width: 849px; height: 1200px; overflow: hidden; background: var(--paper); }
  .poster { position: relative; width: 849px; height: 1200px; background: var(--paper); }

  .tagline {
    position: absolute; right: 59px; top: 81px;
    display: flex; flex-direction: column; align-items: flex-end; gap: 7px;
    font-family: "Marcellus", serif; font-size: 37px; line-height: 41px;
    color: var(--ink-light); text-transform: uppercase;
  }
  .tagline span { background: var(--rust); padding: 0 8px; white-space: nowrap; }

  .portrait {
    position: absolute; left: 81px; top: 170px; width: 607px; height: 594px;
    background:
      radial-gradient(ellipse 55% 50% at 50% 60%, var(--portrait-sepia) 0%, rgba(185,138,106,0.6) 55%, rgba(255,255,255,0) 100%),
      linear-gradient(180deg, var(--portrait-dark) 0%, #6a6a6a 22%, rgba(255,255,255,0) 40%);
    border-radius: 48% 48% 40% 40% / 30% 30% 60% 60%;
  }

  .quote {
    position: absolute; left: 0; top: 773px; width: 849px;
    display: flex; flex-direction: column; align-items: center;
    font-family: "Marcellus", serif; font-size: 78px; line-height: 68px;
    color: var(--ink-light); text-transform: uppercase;
  }
  .quote span { background: var(--rust); padding: 2px 12px 0; white-space: nowrap; }

  .source-rule {
    position: absolute; left: 110px; top: 1128px; width: 624px; height: 10px;
  }
  .source {
    position: absolute; left: 0; top: 1140px; width: 849px; text-align: center;
    font-family: "PT Sans Narrow", sans-serif; font-size: 46px; line-height: 46px;
    color: var(--rust); text-transform: uppercase; letter-spacing: -1px;
  }
</style>
</head>
<body>
<main class="poster">
  <p class="tagline">
    <span>To travel is to discover</span>
    <span>Never lose your enthusiasm</span>
  </p>

  <div class="portrait" role="img" aria-label="Sepia portrait photograph of the quoted author wearing a dark hat and tweed jacket"></div>

  <blockquote class="quote">
    <span>Experience is not</span>
    <span>what happens to</span>
    <span>you. It is what you</span>
    <span>do with what</span>
    <span>happens to you.</span>
  </blockquote>

  <svg class="source-rule" viewBox="0 0 624 10" aria-hidden="true">
    <circle cx="3" cy="3" r="2" fill="#b8501a"/>
    <line x1="12" y1="6" x2="612" y2="6" stroke="#b8501a" stroke-width="1.5"/>
    <circle cx="621" cy="3" r="2" fill="#b8501a"/>
  </svg>
  <p class="source">Ferris Mundell</p>
</main>
</body>
</html>
```